Professional Modern Website Design

We are a premium IT services provider to the financial industry based in London. Our company is called Veltra our current holding page is www.veltra-example.co.uk. We require a new website to match our new corporate identity. This project is for the design phase only. Development will be handled in-house. I have attached examples of wire frames we have developed (although open to suggestions for improvement) Our brand document that should demonstrate current brand, inc how we communicate to potential clients and finally mostly completed web-content.
We are looking for designers that can create something that sets us apart from our competitors.
Target Market(s)
IT Decision makers in Finance companies such as; hedge funds, private investment banks etc
Industry/Entity Type
Financial
Number of Pages Required
5+ page
Requirements
Must have
- hexagon elements in the design, unique design.
Nice to have
- Blog and social media feeds
Should not have
- Should not resemble a downloaded template

```html
<!DOCTYPE html>
<html lang="en">
<head>
<meta charset="utf-8">
<title>Veltra — IT Integration for Finance</title>
<link href="https://fonts.googleapis.com/css2?family=Raleway:wght@400;500;600&family=Open+Sans:wght@400;600&display=swap" rel="stylesheet">
<style>
:root{
  --orange:#f26a21;
  --ink:#222;
  --text:#555;
  --muted:#777;
  --dark:#262626;
  --cyan:#1ccbe3;
  --navy:#1a3c9f;
  --rule:#cfcfcf;
  --white:#fff;
}
*{box-sizing:border-box;margin:0;padding:0}
html,body{width:906px;height:1200px;overflow:hidden;background:var(--white)}
body{position:relative;font-family:"Open Sans",sans-serif;color:var(--text)}
.site-header{position:absolute;left:0;top:0;width:906px;height:74px}
.brand{position:absolute;left:136px;top:12px;display:flex;align-items:center;gap:12px}
.brand-mark{width:44px;height:44px;background:var(--orange)}
.brand-name{font-family:"Raleway",sans-serif;font-weight:400;font-size:20px;letter-spacing:7px;color:#444}
.main-nav{position:absolute;left:390px;top:24px;display:flex;font-family:"Raleway",sans-serif;font-size:11px;font-weight:500;color:var(--ink)}
.main-nav span{padding:6px 14px;height:29px}
.main-nav .active{background:var(--dark);color:var(--white);padding:6px 16px}
.dropdown{position:absolute;left:453px;top:53px;width:216px;height:109px;background:var(--dark);padding:11px 0 0 23px;font-size:8.5px;color:var(--white);line-height:17.8px;z-index:2}
.hero{position:absolute;left:0;top:74px;width:906px;height:385px;background:linear-gradient(180deg,#f7843a 0%,#f25a1d 45%,#f46a24 70%,#f7a04a 100%);text-align:center;color:var(--white)}
.hero h1{position:absolute;top:132px;width:100%;font-family:"Raleway",sans-serif;font-weight:500;font-size:25px;line-height:32px}
.hero h1 .big{font-size:28px}
.hero p{position:absolute;top:201px;left:200px;width:506px;font-size:10px;line-height:14px}
.hero .btn{position:absolute;left:404px;top:243px;width:97px;height:29px;border:2px solid var(--white);font-family:"Raleway",sans-serif;font-size:12.5px;font-weight:500;line-height:25px}
.dots{position:absolute;left:423px;top:362px;display:flex;gap:2px}
.dots i{width:12px;height:12px;border-radius:50%;background:#111}
.dots i:first-child{background:var(--white)}
.who{position:absolute;top:495px;width:906px;text-align:center}
.who h2{font-family:"Raleway",sans-serif;font-weight:400;font-size:19px;color:var(--ink)}
.who .lead{margin:10px auto 0;width:430px;font-size:10.5px;line-height:16px}
.audiences{position:absolute;top:592px;left:140px;display:flex;gap:26px}
.audience{width:134px;text-align:center}
.hex{width:116px;height:128px;margin:0 auto;clip-path:polygon(50% 0,100% 25%,100% 75%,50% 100%,0 75%,0 25%);background:linear-gradient(160deg,#cfd8e2,#6f86a3)}
.audience h3{margin-top:17px;font-family:"Raleway",sans-serif;font-weight:400;font-size:12px;line-height:16px;color:var(--orange)}
.audience p{margin-top:4px;font-size:7px;line-height:12px;color:var(--muted)}
.divider{position:absolute;left:133px;top:853px;width:636px;height:1px;background:var(--rule)}
.blogs{position:absolute;left:137px;top:888px;width:250px}
.blogs h2{font-family:"Raleway",sans-serif;font-weight:500;font-size:15.5px;color:var(--ink);margin-bottom:10px}
.post h3{font-family:"Raleway",sans-serif;font-weight:400;font-size:10.5px;color:var(--orange)}
.post p{font-size:7.5px;line-height:12px;color:var(--muted);margin-top:4px}
.post .date{font-size:9px;color:#444;margin-top:5px}
.post+.post{margin-top:18px}
.feed{position:absolute;top:889px;width:178px;height:182px;border:1px solid #ddd}
.feed h2{height:30px;padding:8px 16px;font-family:"Raleway",sans-serif;font-weight:400;font-size:13px;color:var(--white)}
.feed-pulsar{left:405px}.feed-pulsar h2{background:var(--cyan)}
.feed-circlet{left:594px}.feed-circlet h2{background:var(--navy)}
.item{display:flex;gap:10px;padding:12px 0 0 16px}
.item+.item{padding-top:10px}
.avatar{width:25px;height:23px;flex:none;background:linear-gradient(135deg,#e0b59a,#8a6a58)}
.item p{font-size:7.3px;line-height:11px;color:var(--muted);width:115px}
.item p b{font-weight:400;color:#222}
.item .ago{display:block;margin-top:2px;color:var(--cyan)}
.feed-circlet .ago{color:var(--navy)}
.site-footer{position:absolute;left:0;top:1117px;width:906px;height:83px;background:linear-gradient(180deg,#3a3a3a,#1e1e1e);color:var(--white)}
.footer-nav{position:absolute;left:142px;top:23px;font-size:8px;font-weight:600}
.footer-nav span{margin:0 4px}
.copy{position:absolute;left:142px;top:38px;font-size:7.5px;color:#ddd}
.social{position:absolute;left:706px;top:21px;display:flex;gap:4px}
.social i{width:14px;height:14px;border-radius:2px;background:var(--white)}
</style>
</head>
<body>
<header class="site-header">
  <div class="brand"><div class="brand-mark"></div><span class="brand-name">VELTRA</span></div>
  <nav class="main-nav"><span>ABOUT</span><span class="active">SERVICES</span><span>PARTNERS</span><span>CLIENTS</span><span>CONTACT</span></nav>
  <div class="dropdown">Data centre &amp; infrastructure<br>Support, managed &amp; professional services<br>Voice and data<br>Hosting and cloud<br>Security and IRM</div>
</header>

<section class="hero" role="img" aria-label="Orange-tinted city harbour skyline at dusk">
  <h1>YOU NEED INTEGRATION.<br><span class="big">WE’RE ALWAYS THERE WITH YOU</span></h1>
  <p>Veltra is one of the leading systems integrators to the world’s finance sector. We are an extension of your business and our services portfolio has been built so you always have access to a complete partner</p>
  <div class="btn">About Us</div>
  <div class="dots"><i></i><i></i><i></i><i></i></div>
</section>

<section class="who">
  <h2>WHO ARE YOU?</h2>
  <p class="lead">If you’re part of a financial organisation, we have the power to help everyone work more efficiently, productively and profitably</p>
</section>

<div class="audiences">
  <div class="audience"><div class="hex" role="img" aria-label="Two colleagues reviewing work at a laptop"></div><h3>Senior Hedge Fund Manager/CEO</h3><p>You need to develop and implement strategies for business growth, while ensuring profitability. You’re aware your biggest asset is your staff</p></div>
  <div class="audience"><div class="hex" role="img" aria-label="Portrait of a smiling businesswoman"></div><h3>CFO</h3><p>Your key responsibility is to obtain the maximum ROI from products and services. You understand investment opportunities, providing they return higher efficiencies and revenues.</p></div>
  <div class="audience"><div class="hex" role="img" aria-label="Presenter leading a meeting in an office"></div><h3>IT Manager/CTO</h3><p>Integration with partners and services is your key concern. You want to make sure any IT system you implement will work with the whole infrastructure of your company.</p></div>
  <div class="audience"><div class="hex" role="img" aria-label="Team of employees working together at a desk"></div><h3>Employees</h3><p>You’re working hard, but not getting anywhere fast. You want the tools to make your job easier so you can spend more time thinking about what you’re doing rather than how you’re doing it</p></div>
</div>

<div class="divider"></div>

<section class="blogs">
  <h2>Recent Blogs</h2>
  <article class="post"><h3>Mauris vel lacus vitae felis</h3><p>Class aptent taciti sociosqu ad litora torquent per conubia nostra per inceptos hymenaeos Proin nulla arcu nonummy luctus dictum</p><p class="date">Posted 2 days ago</p></article>
  <article class="post"><h3>Nullam enim leo egestas condimentum</h3><p>Class aptent taciti sociosqu ad litora torquent per conubia nostra per inceptos hymenaeos Proin nulla arcu nonummy luctus</p><p class="date">Posted 2 days ago</p></article>
</section>

<section class="feed feed-pulsar">
  <h2>Pulsar Feed</h2>
  <div class="item"><div class="avatar" role="img" aria-label="User avatar"></div><p><b>Atra per</b> @ inceptos hymenaeos Cum sociis natoque penatibus et magnis dis parturient montes<span class="ago">2 days ago</span></p></div>
  <div class="item"><div class="avatar" role="img" aria-label="User avatar"></div><p><b>Nullam enim leo egestas id condimentum</b> @ inceptos hymenaeos Cum sociis natoque penatibus et magnis dis parturient montes<span class="ago">2 days ago</span></p></div>
</section>

<section class="feed feed-circlet">
  <h2>Circlet Feed</h2>
  <div class="item"><div class="avatar" role="img" aria-label="User avatar"></div><p><b>Lorem ipsum dolor sit amet consectetuer</b> @ inceptos hymenaeos Cum sociis natoque penatibus et magnis dis<span class="ago">2 days ago</span></p></div>
  <div class="item"><div class="avatar" role="img" aria-label="User avatar"></div><p><b>Quisque dignissim congue</b> @ inceptos hymenaeos Cum sociis natoque penatibus et magnis dis parturient montes<span class="ago">2 days ago</span></p></div>
</section>

<footer class="site-footer">
  <nav class="footer-nav">HOME<span>|</span>OUR SERVICES<span>|</span>ABOUT US<span>|</span>OUR TEAM<span>|</span>JOIN US<span>|</span>CONTACT</nav>
  <p class="copy">© 2015 Company Name &nbsp;All right reserved &nbsp;Term of Use</p>
  <div class="social" aria-label="Social links"><i></i><i></i><i></i></div>
</footer>
</body>
</html>
```